Crestline Gas and Plumbing Business Card Design

I am after a business card design for my plumbing business called 'Crestline Gas & Plumbing'. I do all types of plumbing and gas work and specialise in general maintenance plumbing. Would like to see designs using current logo

Industry/Entity Type

Plumbing

Contact Information for Business Card

Name - Dale Whitcombe
Phone number - 0455163027
Email - admin@crestlinegasandplumbing.example.com.au
ABN - 68204915336

```html
<!DOCTYPE html>
<html lang="en">
<head>
<meta charset="utf-8">
<title>Crestline Gas &amp; Plumbing – Business Card</title>
<link href="https://fonts.googleapis.com/css2?family=Lato:wght@400;700&display=swap" rel="stylesheet">
<style>
  :root {
    --backdrop: #ececec;
    --card: #ffffff;
    --brand-blue: #2a4ea3;
    --ink: #1c1c1c;
    --brand-orange: #f08a1c;
    --faint-mark: #f4e6d8;
  }
  * { margin: 0; padding: 0; box-sizing: border-box; }
  html, body {
    width: 1200px; height: 944px; overflow: hidden;
    background: var(--backdrop);
    font-family: "Lato", Arial, sans-serif;
  }
  .canvas { position: relative; width: 1200px; height: 944px; }
  .card {
    position: absolute; left: 320px; width: 616px; height: 358px;
    background: var(--card);
    box-shadow: 0 6px 18px rgba(0,0,0,0.18);
  }
  .card--front { top: 108px; }
  .card--back { top: 498px; }

  .brand {
    display: flex; align-items: center; gap: 10px;
    color: var(--brand-blue); font-weight: 700; white-space: nowrap;
  }
  .brand__dot {
    border-radius: 50%; background: var(--brand-orange); flex: none;
  }
  .card--front .brand { position: absolute; left: 46px; top: 60px; font-size: 21px; }
  .card--front .brand__dot { width: 22px; height: 22px; }
  .card--back .brand {
    position: absolute; left: 0; right: 0; top: 152px;
    justify-content: center; font-size: 34px; gap: 14px;
  }
  .card--back .brand__dot { width: 36px; height: 36px; }

  .abn {
    position: absolute; right: 34px; top: 20px;
    font-size: 15px; color: var(--ink);
  }
  .holder {
    position: absolute; left: 50px; top: 220px;
    font-size: 25px; font-weight: 700; color: var(--brand-blue);
  }
  .contact {
    position: absolute; left: 47px; top: 266px;
    list-style: none; font-size: 14.5px; color: var(--ink);
  }
  .contact li { display: flex; align-items: center; gap: 10px; height: 20px; }
  .contact svg { width: 12px; height: 12px; fill: var(--brand-blue); flex: none; }
  .faint-mark {
    position: absolute; left: 482px; top: 180px;
    width: 92px; height: 92px; border-radius: 50%;
    background: var(--faint-mark);
  }
</style>
</head>
<body>
<main class="canvas">
  <section class="card card--front" aria-label="Business card front">
    <div class="brand"><span class="brand__dot"></span>Crestline Gas &amp; Plumbing</div>
    <p class="abn">ABN - 68204915336</p>
    <h1 class="holder">Dale Whitcombe</h1>
    <ul class="contact">
      <li>
        <svg viewBox="0 0 24 24" aria-hidden="true"><path d="M6.6 10.8a15.1 15.1 0 0 0 6.6 6.6l2.2-2.2c.3-.3.7-.4 1-.2 1.1.4 2.3.6 3.6.6.6 0 1 .4 1 1V20c0 .6-.4 1-1 1A17 17 0 0 1 3 4c0-.6.4-1 1-1h3.5c.6 0 1 .4 1 1 0 1.3.2 2.5.6 3.6.1.3 0 .7-.2 1z"/></svg>
        0455163027
      </li>
      <li>
        <svg viewBox="0 0 24 24" aria-hidden="true"><path d="M2 5h20v14H2z M2 5l10 8 10-8" fill="none" stroke="#2a4ea3" stroke-width="2"/></svg>
        admin@crestlinegasandplumbing.example.com.au
      </li>
    </ul>
    <div class="faint-mark" aria-hidden="true"></div>
  </section>

  <section class="card card--back" aria-label="Business card back">
    <div class="brand"><span class="brand__dot"></span>Crestline Gas &amp; Plumbing</div>
  </section>
</main>
</body>
</html>
```